Safety training business card design

We need a buisness card design and logo for a small buisness that provides safety training through out the mining and civil construction industries. We provide first aid , confined space working at heights , machinery tickets, chainsaw, four wheel drive and four wheel motorbike training. We would like to use the design colors of navy blue, Fluro or lime green and white .

Industry/Entity Type

Construction

Contact Information for Business Card

Rillford Groundworks & Training , Neville Ormsby, rillford.skills@mailbox-example.net, ph 0481065374 abn 47 806 315 914

```html
<!DOCTYPE html>
<html lang="en">
<head>
<meta charset="utf-8">
<title>Rillford Groundworks &amp; Training — Business Card</title>
<link rel="stylesheet" href="https://fonts.googleapis.com/css2?family=Roboto+Condensed:wght@300;400;700&display=swap">
<style>
  :root {
    --backdrop: #d4d4d4;
    --card-green: #22b24c;
    --navy: #1a0b5b;
    --card-shadow: rgba(0, 0, 0, 0.28);
  }
  html, body {
    margin: 0;
    padding: 0;
    width: 1200px;
    height: 953px;
    overflow: hidden;
    background: var(--backdrop);
  }
  .canvas {
    position: relative;
    width: 1200px;
    height: 953px;
    font-family: "Roboto Condensed", "Arial Narrow", sans-serif;
    color: var(--navy);
  }
  .card {
    position: absolute;
    left: 376px;
    width: 445px;
    height: 268px;
    background: var(--card-green);
    box-shadow: 8px 10px 18px var(--card-shadow);
  }
  .card--front { top: 173px; }
  .card--back  { top: 512px; }

  .brand-square {
    position: absolute;
    left: 96px;
    top: 86px;
    width: 96px;
    height: 96px;
    background: var(--navy);
  }
  .brand-name {
    position: absolute;
    left: 259px;
    top: 96px;
    margin: 0;
    font-weight: 700;
    font-size: 21px;
    line-height: 26px;
    letter-spacing: 0.4px;
    text-transform: uppercase;
  }

  .back-company {
    position: absolute;
    left: 82px;
    top: 66px;
    margin: 0;
    font-weight: 700;
    font-size: 9.5px;
    letter-spacing: 0.3px;
    text-transform: uppercase;
  }
  .back-person {
    position: absolute;
    left: 82px;
    top: 118px;
    margin: 0;
    font-weight: 400;
    font-size: 30px;
    line-height: 36px;
  }
  .back-contact {
    position: absolute;
    left: 82px;
    top: 174px;
    margin: 0;
    font-weight: 300;
    font-size: 16px;
    line-height: 22px;
  }
</style>
</head>
<body>
<main class="canvas">
  <section class="card card--front" aria-label="Card front">
    <div class="brand-square"></div>
    <h1 class="brand-name">Rillford<br>Groundworks<br>&amp; Training</h1>
  </section>

  <section class="card card--back" aria-label="Card back">
    <p class="back-company">Rillford Groundworks &amp; Training</p>
    <h2 class="back-person">Neville Ormsby</h2>
    <p class="back-contact">rillford.skills@mailbox-example.net<br>ph 0481065374 abn 47 806 315 914</p>
  </section>
</main>
</body>
</html>
```